Breakfast Menu at a Bar and Grill

6" x 9" flyer
The attached powerpoint file contains slides with the text to be included in the front and back of the flyer. I will leave it to the designer to suggest color and background designs. Marlowe's Quiet Corner is a no frills dive bar with a blue color customer base. A simple breakfast theme will do.

Target Market(s)

Seniors and blue collar workers.

Font styles to use
Decorative

Colors

Designer to choose colors to be used in the design.

Requirements
Must have
• Our Logo (attached jpg) and the text in the attached PowerPoint file. Some kind of breakfast dish as the background. I will rely on the designers regards the font sizes.
Nice to have
• The background design should have a pic of a breakfast plate that matches one of the items on special...perhaps two pics?
Should not have
• pic that shows food that is not listed on the flyer.

```html
<!DOCTYPE html>
<html lang="en">
<head>
<meta charset="utf-8">
<title>Marlowe's Quiet Corner – Breakfast Specials Flyer</title>
<link href="https://fonts.googleapis.com/css2?family=Kaushan+Script&family=Pinyon+Script&family=Lato:wght@400;700;900&family=Playfair+Display:ital,wght@1,700&display=swap" rel="stylesheet">
<style>
  :root {
    --orange: #f28023;
    --paper: #f6f6f6;
    --ink: #1c1c1c;
    --white: #ffffff;
    --accent: #f08224;
    --pancake: #c07a3e;
    --pancake-light: #e2ad70;
    --omelet: #f1c76f;
    --omelet-light: #f8e2a8;
    --drink-red: #c9413a;
    --drink-amber: #e7a84a;
    --drink-lime: #cfd66a;
  }
  * { margin: 0; padding: 0; box-sizing: border-box; }
  html, body { width: 1200px; height: 1200px; overflow: hidden; background: var(--white); }
  .canvas { position: relative; width: 1200px; height: 1200px; font-family: "Lato", sans-serif; color: var(--ink); }

  .panel { position: absolute; top: 149px; height: 784px; box-shadow: 0 2px 6px rgba(0,0,0,.22); overflow: hidden; }
  .panel--front { left: 29px; width: 571px; background: var(--paper); }
  .panel--back { left: 614px; width: 555px; background: var(--orange); }

  .front-header { position: absolute; left: 0; top: 0; width: 571px; height: 232px; background: var(--orange); }
  .front-title { position: absolute; left: 0; top: 34px; width: 571px; text-align: center; font-family: "Kaushan Script", cursive; font-weight: 400; font-size: 49px; line-height: 1.1; color: var(--white); white-space: nowrap; }
  .specials-title { position: absolute; left: 30px; top: 106px; width: 290px; text-align: center; font-family: "Pinyon Script", cursive; font-size: 40px; color: var(--white); line-height: 1; }
  .specials-hours { position: absolute; left: 30px; top: 150px; width: 282px; text-align: center; font-weight: 900; font-size: 27px; color: var(--white); }
  .header-divider { position: absolute; left: 337px; top: 115px; width: 1px; height: 80px; background: rgba(255,255,255,.7); }
  .header-offer { position: absolute; right: 42px; top: 113px; width: 190px; text-align: right; font-size: 11.5px; line-height: 14px; color: var(--white); white-space: nowrap; }

  .section-title { position: absolute; font-family: "Playfair Display", serif; font-style: italic; font-weight: 700; font-size: 21px; color: var(--accent); letter-spacing: .5px; transform: translateX(-50%); white-space: nowrap; }
  .menu-list { position: absolute; left: 47px; width: 301px; list-style: none; }
  .menu-item { display: flex; justify-content: space-between; font-size: 16px; letter-spacing: .2px; }
  .menu-list--food .menu-item { height: 24.5px; }
  .menu-list--drinks .menu-item { height: 21px; }

  .dish-photo { position: absolute; border-radius: 14px; }
  .dish-photo--pancakes { left: 371px; top: 311px; width: 168px; height: 104px; background: linear-gradient(180deg, var(--pancake-light) 0%, var(--pancake) 100%); }
  .dish-photo--omelet { left: 375px; top: 497px; width: 172px; height: 86px; background: linear-gradient(180deg, var(--omelet-light) 0%, var(--omelet) 100%); }
  .dish-photo--drinks { left: 379px; top: 647px; width: 140px; height: 90px; background: linear-gradient(90deg, var(--drink-red) 0%, var(--drink-amber) 50%, var(--drink-lime) 100%); }

  .brand-mark { position: absolute; left: 146px; top: 206px; width: 262px; display: flex; align-items: center; justify-content: center; gap: 12px; }
  .brand-dot { width: 22px; height: 22px; border-radius: 50%; background: var(--white); }
  .brand-name { font-family: "Lato", sans-serif; font-weight: 900; font-size: 38px; color: var(--white); }

  .address-band { position: absolute; left: 18px; top: 695px; width: 520px; height: 50px; background: linear-gradient(90deg, var(--orange) 0%, #fdf1e6 28%, #ffffff 45%, #fbe3cc 72%, #f6a25c 100%); text-align: center; }
  .address-line { font-size: 17.5px; line-height: 22px; padding-top: 3px; }
  .phone-line { font-size: 17.5px; font-weight: 900; line-height: 22px; }
</style>
</head>
<body>
<div class="canvas">

  <section class="panel panel--front">
    <div class="front-header"></div>
    <h1 class="front-title">Marlowe's Quiet Corner</h1>
    <p class="specials-title">Breakfast Specials</p>
    <p class="specials-hours">6AM – 11AM</p>
    <div class="header-divider"></div>
    <p class="header-offer">Free Breakfast on Sunday with<br>a two drink purchase. Monday<br>through Saturday;<br>Purchase a breakfast special<br>item with a two drink minimum<br>and get one free.</p>

    <h2 class="section-title" style="left:211px; top:265px;">Traditional Favorites</h2>
    <ul class="menu-list menu-list--food" style="top:306px;">
      <li class="menu-item"><span>THE 5-STAR BREAKFAST</span><span>$5.50</span></li>
      <li class="menu-item"><span>PANCAKES W/BACON</span><span>$5.50</span></li>
      <li class="menu-item"><span>2 EGGS BACON OR SAUSAGE</span><span>$5.50</span></li>
      <li class="menu-item"><span>3 PANCAKES</span><span>$4.00</span></li>
      <li class="menu-item"><span>3 FRENCH TOAST</span><span>$4.00</span></li>
    </ul>
    <div class="dish-photo dish-photo--pancakes" role="img" aria-label="Photo of a stack of pancakes with syrup, strawberries and blueberries"></div>

    <h2 class="section-title" style="left:183px; top:443px;">Omelets</h2>
    <ul class="menu-list menu-list--food" style="top:480px;">
      <li class="menu-item"><span>CALIFORNIA OMELET</span><span>$6.00</span></li>
      <li class="menu-item"><span>GREEN CHILI OMELET</span><span>$6.00</span></li>
      <li class="menu-item"><span>PUEBLO OMELET</span><span>$6.00</span></li>
      <li class="menu-item"><span>SPANISH OMELET</span><span>$6.00</span></li>
      <li class="menu-item"><span>BASIC BREAKFAST OMELET</span><span>$6.00</span></li>
    </ul>
    <div class="dish-photo dish-photo--omelet" role="img" aria-label="Photo of a folded omelet with tomato and cucumber garnish"></div>

    <h2 class="section-title" style="left:193px; top:617px;">Drink Specials</h2>
    <ul class="menu-list menu-list--drinks" style="top:653px;">
      <li class="menu-item"><span>DOMESTIC BOTTLES</span><span>$1.75</span></li>
      <li class="menu-item"><span>DOMESTIC DRAFTS</span><span>$2.00</span></li>
      <li class="menu-item"><span>WELL DRINKS</span><span>$3.00</span></li>
      <li class="menu-item"><span>SCREWDRIVERS</span><span>$3.00</span></li>
    </ul>
    <div class="dish-photo dish-photo--drinks" role="img" aria-label="Photo of assorted cocktails and mixed drinks"></div>
  </section>

  <section class="panel panel--back">
    <div class="brand-mark">
      <span class="brand-dot"></span>
      <span class="brand-name">Marlowe's</span>
    </div>
    <div class="address-band">
      <p class="address-line">4810 N JUNIPER MESA RD. | TEMPE FLATS, AZ 85099</p>
      <p class="phone-line">602-555-0148</p>
    </div>
  </section>

</div>
</body>
</html>
```